Poster and Logo for a Football Fan Park

Please design a poster similar to the attached idea. The poster will be for a football fan park in Mozambique during the ARBE Meridan Shield 2014.

Please use Mozambican/Brazilian colours in the poster and include a logo for the fan park. The name if the fan park is "Brisa Cajueiro" and is situated in the village of "Moatize". Any writing/slogans on the poster must be in Portuguese. Please include the dates (12 Junho 2014 - 13 Julho 2014).

The poster must not include the words "ARBE" or "Meridan Shield".

Target Market(s)

Mozambican Middle to Upper class citizens
Expatriates working in Mozambique

Industry/Entity Type

Graphic Design

Requirements
Must have
• Feeling of lively, enthusiastic, partying football crowd.
• Mozambican national flag colours.
• Dates of ARBE Soccer Meridan Shield 2014
Should not have
• Any official ARBE branding or trademarks that will require a licence.

```html
<!DOCTYPE html>
<html lang="pt">
<head>
<meta charset="utf-8">
<title>Brisa Cajueiro — Moatize</title>
<link href="https://fonts.googleapis.com/css2?family=Arimo:wght@700&display=swap" rel="stylesheet">
<style>
  :root {
    --sun-core: #ffd21a;
    --sun-mid: #f2661e;
    --sun-red: #e0281f;
    --sun-edge: #7a1a13;
    --crowd-white: #f4f4f4;
    --crowd-green: #1f9a49;
    --crowd-yellow: #fcc813;
    --crowd-black: #141414;
    --ink: #000000;
    --paper: #ffffff;
  }
  html, body {
    margin: 0;
    padding: 0;
    width: 1200px;
    height: 847px;
    overflow: hidden;
    background: var(--paper);
  }
  .poster {
    position: relative;
    width: 1200px;
    height: 847px;
    overflow: hidden;
    background: radial-gradient(circle at 50% 17%, var(--sun-core) 0%, var(--sun-mid) 13%, var(--sun-red) 38%, var(--sun-edge) 100%);
    font-family: "Arimo", Arial, sans-serif;
    font-weight: 700;
  }
  .crowd {
    position: absolute;
    left: 0;
    top: 0;
    width: 1200px;
    height: 847px;
  }
  .ball {
    position: absolute;
    left: 498px;
    top: 32px;
    width: 204px;
    height: 204px;
  }
  .headline {
    position: absolute;
    left: 0;
    width: 100%;
    text-align: center;
    margin: 0;
    color: var(--paper);
    -webkit-text-stroke: 8px var(--ink);
    paint-order: stroke fill;
    line-height: 1;
  }
  .headline--name { top: 250px; font-size: 72px; letter-spacing: 0.5px; }
  .headline--place { top: 332px; font-size: 44px; -webkit-text-stroke-width: 6px; }
  .headline--dates { top: 383px; font-size: 27px; -webkit-text-stroke-width: 5px; }
  .headline--soon {
    top: 420px;
    font-size: 132px;
    color: var(--ink);
    -webkit-text-stroke: 12px var(--paper);
    letter-spacing: 1px;
  }
</style>
</head>
<body>
  <main class="poster">
    <svg class="crowd" viewBox="0 0 1200 847" role="img" aria-label="Multidão de adeptos em silhuetas brancas, verdes, amarelas e pretas a festejar com bandeiras">
      <defs>
        <linearGradient id="crowdTone" x1="0" y1="290" x2="0" y2="847" gradientUnits="userSpaceOnUse">
          <stop offset="0" stop-color="var(--crowd-white)"/>
          <stop offset="0.12" stop-color="var(--crowd-green)"/>
          <stop offset="0.42" stop-color="var(--crowd-green)"/>
          <stop offset="0.56" stop-color="var(--crowd-yellow)"/>
          <stop offset="0.76" stop-color="var(--crowd-yellow)"/>
          <stop offset="0.9" stop-color="var(--crowd-black)"/>
          <stop offset="1" stop-color="var(--crowd-black)"/>
        </linearGradient>
      </defs>
      <path d="M0 290 C 120 270, 200 330, 260 420 C 330 520, 420 560, 520 575 C 600 585, 680 570, 760 540 C 880 500, 960 420, 1020 340 C 1080 300, 1150 300, 1200 320 L 1200 847 L 0 847 Z" fill="url(#crowdTone)"/>
    </svg>

    <svg class="ball" viewBox="0 0 204 204" role="img" aria-label="Bola de futebol preta e branca">
      <defs>
        <radialGradient id="ballTone" cx="0.42" cy="0.36" r="0.72">
          <stop offset="0" stop-color="#ffffff"/>
          <stop offset="0.55" stop-color="#bdbdbd"/>
          <stop offset="0.85" stop-color="#555555"/>
          <stop offset="1" stop-color="#1a1a1a"/>
        </radialGradient>
      </defs>
      <circle cx="102" cy="102" r="100" fill="url(#ballTone)"/>
    </svg>

    <h1 class="headline headline--name">Brisa Cajueiro</h1>
    <p class="headline headline--place">Moatize</p>
    <p class="headline headline--dates">12 Junho 2014 - 13 Julho 2014</p>
    <p class="headline headline--soon">Em Breve</p>
  </main>
</body>
</html>
```